Erstellung eines responsiven One-Pagers für mittelständiges Unternehmen im Bauhauptgewerbe
Zielgruppe
Seit fast 30 Jahren sind wir als mittelständiges Unternehmen im Bauhauptgewerbe tätig.
Aufgabenstellung
Die bestehende Webseite soll einen Relaunch bekommen. Dazu entnehmen Sie bitte Bildmaterial und Logo aus der alten Seite. Wir würden gerne daraus einen responsiven One-Pager bauen.
Da die alte Seite jetzt schon 10 Jahre alt ist, würden wir gerne ein neues Design erstellen lassen. Später werden wir es entweder selbst von unserem Programmierer entwickeln lassen oder Sie erstellen uns ein Angebot. Das Design sollte auch so aufgebaut sein, dass es responsive funktionieren würde.

```html
<!DOCTYPE html>
<html lang="de">
<head>
<meta charset="utf-8">
<title>K+W Bautenschutz GmbH</title>
<link rel="stylesheet" href="https://fonts.googleapis.com/css2?family=PT+Sans:ital,wght@0,400;0,700;1,400;1,700&display=swap">
<style>
:root{
  --navy:#13284b;
  --blue:#2e5cab;
  --link:#1f3f85;
  --text:#333a44;
  --muted:#8a8f98;
  --line:#c3c7cd;
  --white:#ffffff;
}
*{box-sizing:border-box;margin:0;padding:0}
html,body{width:1200px;height:4688px;overflow:hidden;background:var(--white)}
body{position:relative;font-family:"PT Sans",Arial,sans-serif;color:var(--text);font-size:9.5px;line-height:13px}
.abs{position:absolute}

/* header */
.site-header{position:absolute;left:0;top:0;width:1200px;height:105px}
.brand{position:absolute;left:142px;top:36px;display:flex;align-items:center;gap:10px;color:var(--navy);font-size:21px;font-weight:700}
.brand-square{width:16px;height:16px;background:var(--blue)}
.header-divider{position:absolute;left:426px;top:20px;width:1px;height:64px;background:var(--line)}
.tagline{position:absolute;left:453px;top:44px;font-size:15px;font-style:italic;color:var(--navy);letter-spacing:.2px}
.tagline span{color:var(--muted);padding:0 4px}

/* nav */
.nav-top{position:absolute;left:0;top:104px;width:1200px;height:5px;background:var(--blue)}
.main-nav{position:absolute;left:0;top:109px;width:1200px;height:51px;background:var(--navy);color:var(--white)}
.nav-item{position:absolute;top:0;height:51px;width:143px;display:flex;align-items:center;justify-content:center;font-size:12.5px;text-transform:uppercase;border-left:1px solid #3b5078}
.nav-item.last{border-right:1px solid #3b5078}
.nav-contact{position:absolute;left:812px;top:20px;font-size:9.5px}
.nav-contact svg{vertical-align:-1px;margin-right:3px}

/* hero */
.hero{position:absolute;left:0;top:160px;width:1200px;height:364px;background:linear-gradient(180deg,#5c7fb4 0%,#9fb7d4 30%,#c9cfd3 55%,#8e8f8b 80%,#6f6e68 100%)}
.hero-line{position:absolute;left:0;top:524px;width:1200px;height:6px;background:var(--blue)}
.pager{display:flex;align-items:center;gap:9px;font-size:11px;color:var(--navy)}
.pager .num{width:15px;height:15px;display:flex;align-items:center;justify-content:center}
.pager .num.active{background:var(--navy);color:var(--white)}
.hero .pager{position:absolute;left:532px;top:330px;color:var(--white)}
.hero .pager .num.active{background:var(--navy)}

/* sections */
.section{position:absolute;left:0;width:1200px}
.section-head{display:flex;align-items:flex-start;height:26px}
.head-bar{height:15px;background:var(--navy);margin-top:3px}
.head-bar.left{width:276px}
.head-bar.right{flex:1}
.section-title{padding:0 10px;font-size:23px;line-height:22px;color:var(--navy);text-transform:uppercase;letter-spacing:.5px}
.content{position:absolute;left:286px;width:386px}
.subtitle{font-size:12.5px;font-weight:700;color:var(--navy);line-height:16px}
.intro{font-weight:700;color:var(--navy);margin-top:14px}
p{margin-top:10px}
.small-head{font-weight:700;color:var(--navy);margin-top:14px}
.block-head{font-size:12.5px;font-weight:700;color:var(--navy);line-height:16px}

.photo{position:absolute;background:var(--white);padding:6px;box-shadow:0 1px 5px rgba(0,0,0,.35)}
.photo div{width:100%;height:100%}

.num-list{list-style:none;margin-top:12px}
.num-list li{display:flex;align-items:center;gap:9px;height:22.5px;color:var(--link)}
.num-list .badge{width:15px;height:15px;background:var(--navy);color:var(--white);display:flex;align-items:center;justify-content:center;font-size:9px;font-weight:700}

.arrow-l,.arrow-r{width:0;height:0;border-top:11px solid transparent;border-bottom:11px solid transparent}
.arrow-l{border-right:11px solid var(--navy)}
.arrow-r{border-left:11px solid var(--navy)}

.cmp-label{position:absolute;font-weight:700;color:var(--navy)}
.thumbs{position:absolute;left:351px;display:flex}
.thumbs div{width:64.5px;height:46px;border-left:1px solid #fff}
.thumbs .sel{position:absolute;left:0;top:-2px;width:131px;height:50px;border:2px solid var(--blue)}
.slide-arrow{position:absolute;width:0;height:0;border-top:10px solid transparent;border-bottom:10px solid transparent}
.slide-arrow.l{left:286px;border-right:10px solid #8d96a6}
.slide-arrow.r{left:926px;border-left:10px solid #8d96a6}

/* contact */
.address{display:flex;gap:82px;margin-top:20px}
.address td{padding-right:14px}
.field{position:absolute;height:26px;border:1px solid var(--line);font-style:italic;color:var(--muted);padding:6px 4px;font-size:9.5px}
.captcha{position:absolute;left:286px;top:3043px;width:180px;height:42px;background:#f9f9f9;border:1px solid #d3d3d3;border-radius:3px;box-shadow:0 0 3px rgba(0,0,0,.1);font-size:8.5px;color:#444}
.captcha .box{position:absolute;left:8px;top:12px;width:16px;height:16px;border:2px solid #c1c1c1;background:#fff;border-radius:2px}
.captcha .label{position:absolute;left:32px;top:14px}
.captcha .mark{position:absolute;left:140px;top:7px;width:16px;height:16px;background:#8aa6d6}
.captcha .fine{position:absolute;left:124px;top:27px;font-size:5.5px;line-height:6px;color:#777}
.submit{position:absolute;left:477px;top:3043px;width:178px;height:42px;background:var(--navy);color:var(--white);font-weight:700;font-size:12px;display:flex;align-items:center;justify-content:center}
.map{position:absolute;left:286px;top:3132px;width:369px;height:208px;border:1px solid var(--line);background:linear-gradient(135deg,#eef0ea,#e2e6de 60%,#d9e4d0)}

/* footer */
.site-footer{position:absolute;left:0;top:3775px;width:1200px;height:122px;background:var(--navy);color:var(--white)}
.foot-links{position:absolute;left:0;top:54px;width:1200px;display:flex;justify-content:center;font-size:12px;text-transform:uppercase}
.foot-links span{padding:0 11px;border-left:1px solid #fff;line-height:22px}
.foot-links span:first-child{border-left:none}
.copyright{position:absolute;left:0;top:104px;width:1200px;text-align:center;font-size:8.5px}
</style>
</head>
<body>

<header class="site-header">
  <div class="brand"><span class="brand-square"></span>K+W Bautenschutz GmbH</div>
  <div class="header-divider"></div>
  <div class="tagline">Seit über 20 Jahren: Betoninstandsetzung<span>|</span>Spritzbeton<span>|</span>Brückensanierung<span>|</span>Balkone<span>|</span>Abdichtung</div>
</header>

<div class="nav-top"></div>
<nav class="main-nav">
  <div class="nav-item" style="left:142px">Unternehmen</div>
  <div class="nav-item" style="left:285px">Referenzen</div>
  <div class="nav-item" style="left:428px">Leistungen</div>
  <div class="nav-item last" style="left:570px">Kontakt</div>
  <div class="nav-contact">
    <svg width="9" height="9" viewBox="0 0 10 10"><path d="M2 0l2 2.5-1.2 1.3c.6 1.4 1.6 2.4 3 3L7.1 5.6 9.6 7.6 8.6 9.6C4 9.6.4 6 .4 1.4z" fill="#fff"/></svg>(0 62 05) 41 18 20&nbsp;&nbsp;|&nbsp;&nbsp;<svg width="10" height="9" viewBox="0 0 10 9"><rect x="2" y="0" width="6" height="3" fill="#fff"/><rect x="0" y="3" width="10" height="4" fill="#fff"/><rect x="2" y="6" width="6" height="3" fill="#fff" stroke="#13284b" stroke-width=".6"/></svg>(0 62 05) 41 18 21&nbsp;&nbsp;|&nbsp;&nbsp;<svg width="10" height="8" viewBox="0 0 10 8"><rect width="10" height="8" fill="#fff"/><path d="M0 0l5 4 5-4" stroke="#13284b" fill="none"/></svg>info@kw-bautenschutz.de
  </div>
</nav>

<section class="hero" role="img" aria-label="Foto: Firmenhalle mit Lieferwagen und Mitarbeitern vor dem Betriebsgelände">
  <div class="pager">
    <div class="arrow-l" style="border-right-color:var(--navy)"></div>
    <div class="num active">1</div><div class="num">2</div><div class="num">3</div><div class="num">4</div>
    <div class="arrow-r"></div>
  </div>
</section>
<div class="hero-line"></div>

<!-- Unternehmen -->
<section class="section" style="top:565px">
  <div class="section-head"><div class="head-bar left"></div><h2 class="section-title">Unternehmen</h2><div class="head-bar right"></div></div>
  <div class="content" style="top:29px">
    <div class="subtitle">Betonsanierung in Heidelberg, Mannheim und Umgebung</div>
    <div class="intro" style="margin-top:17px">Langfristige Betonerhaltung durch Instandsetzung und Korrosionsschutz</div>
    <p>Sie sind richtig bei uns wenn wir über folgende Begriffe sprechen. Betonschäden, Balkonschäden, Betonschutz- und Instandsetzung, Betonkosmetik, Betonsanierung, Balkone, Brücken, Brandschäden, SIVV, PCC, SPCC und Spritzbeton.</p>
    <p>Als Untergrundvorbereitung, bei jeder Instandhaltungsmaßnahme, ist eine Reinigung erforderlich. Hierbei kommt das Sandstrahlen, Druckluftstrahlen, Wasserstrahlen, Fräsen oder Schleifen zum Einsatz.</p>
    <p>Weitere Themen im Bereich der Abdichtung sind die Bodenbeschichtung, Bauwerksabdichtung, Horizontalsperre, Verpelung, Risse, Injektion mit Harz oder Zementleim / Zementsuspension, dauerelastische Fugen, Kellerabdichtung, KMB - Beschichtung und Dichtungsschlämme</p>
  </div>
  <div class="photo" style="left:715px;top:67px;width:220px;height:147px"><div role="img" aria-label="Foto: Baustelle mit Betonwänden und Bewehrung" style="background:linear-gradient(160deg,#7d7a74,#a9a59c 50%,#6e6a62)"></div></div>
</section>

<!-- Leistungen -->
<section class="section" style="top:824px">
  <div class="section-head"><div class="head-bar left"></div><h2 class="section-title">Leistungen</h2><div class="head-bar right"></div></div>
  <div class="content" style="top:29px">
    <div class="subtitle">Arbeiten im Privat-, Hoch-, und Ingenieurbau</div>
    <p style="margin-top:17px">Wir führen Arbeiten im Privat-, Hoch-, und Ingenieurbau aus. Aber auch als Generalunternehmer für verschiedene Gewerke sind wir aktiv. Die Erstellung von Leistungsverzeichnissen ist ebenfalls möglich.</p>
    <p>Gerne beraten wir Sie ausführlich zu Ihrem Bauvorhaben und informieren Sie kompetent über die Möglichkeiten, Ihr Projekt umzusetzen.</p>
    <p>Klicken Sie sich durch unser Leistungsangebot:</p>
    <ul class="num-list">
      <li><span class="badge">1</span>Brückensanierung &amp; Korrosionsschutz</li>
      <li><span class="badge">2</span>Statische Spritzbetonverstärkungen</li>
      <li><span class="badge">3</span>Beton- &amp; Balkoninstandsetzung</li>
      <li><span class="badge">4</span>Horizontalsperren, Beschichtung, Kellerabdichtung</li>
    </ul>
    <div class="block-head" style="margin-top:20px">Brückensanierung &amp; Korrosionsschutz</div>
    <div class="small-head" style="margin-top:18px">Brückensanierung</div>
    <p>Brücken werden durch den zunehmenden Verkehr, besonders durch die Traglast von Lastwagen immer stärker beansprucht. Deshalb ist eine regelmäßige Kontrolle und Ausbesserung der Schäden unverzichtbar. Wir setzen mit unserer langjähriger Erfahrung Brücken kompetent in Stand oder erneuern sie bei Bedarf, um sie für die tägliche Beanspruchung wieder tauglich und sicher zu machen.</p>
    <p>Grundlage für die Instandsetzung von Brückenbauwerken ist die ZTV-ING. Hierbei handelt es sich um zusätzliche technische Vertragsbedingungen und Richtlinien für Ingenieurbauten, Stand: Dezember 2007. Alle notwendigen Produkte für die Ausführung werden geprüft und in der aktuellen BASt-Liste aufgeführt. Die ZTV-ING gelten für den Bau und die Erhaltung von Ingenieurbauten nach DIN 1076. Darin sind sämtliche Zusätzlichen Technischen Vertragsbedingungen (ZTV), alle Technischen Lieferbedingungen und Technischen Prüfvorschriften (TL/TP) enthalten.</p>
    <div class="small-head">Korrosionsschutz</div>
    <p>Bei einer Korrosion reagiert Metall mit seiner Umgebung, wodurch es zu Beschädigungen der Oberfläche kommen kann. Um eine Beeinträchtigung der Funktionalität eines Bauteiles zu vermeiden, werden mit dem Korrosionsschutz Maßnahmen getroffen, um Schäden zu vermeiden bzw. so gut wie möglich hinauszuzögern.</p>
    <p>Für den Korrosionsschutz gelten die DIN EN ISO 12944 und der ZTV-KOR Stahlbauten. Man spricht hierbei von schwerem Korrosionsschutz, als Beispiel beim Brückengeländer. Beschichtungsvorschläge für den Stahl sind hier, die Untergrundvorbehandlung durch Druckluftstrahlen im Reinheitsgrad Sa 2 ½, eine Grundierung, ein oder zwei Zwischenanstriche und ein Deckanstrich. Die Produkte können 1-komponentig, 2-komponentig oder im System als Hydro-Beschichtung zur Ausführung gelangen.</p>
    <div class="pager" style="margin-top:52px">
      <div class="arrow-l"></div><div class="num">1</div><div class="num">2</div><div class="num">3</div><div class="num">4</div><div class="arrow-r"></div>
    </div>
  </div>
  <div class="photo" style="left:715px;top:64px;width:220px;height:149px"><div role="img" aria-label="Foto: sanierter mehrstöckiger Bürobau" style="background:linear-gradient(180deg,#7f9fc9,#b9c2c8 40%,#8c9579 85%,#5f6f43)"></div></div>
  <div class="photo" style="left:715px;top:272px;width:220px;height:142px"><div role="img" aria-label="Foto: Brückenunterseite über einem Bach" style="background:linear-gradient(180deg,#9aa299,#6e7466 50%,#4d5a3b)"></div></div>
  <div class="photo" style="left:715px;top:428px;width:220px;height:140px"><div role="img" aria-label="Foto: Betonbrücke mit Geländer" style="background:linear-gradient(180deg,#8f948f,#6b6a63 55%,#575b4a)"></div></div>
  <div class="photo" style="left:715px;top:583px;width:220px;height:145px"><div role="img" aria-label="Foto: Treppenanlage aus Beton mit Geländer" style="background:linear-gradient(180deg,#c7ccc6,#9da390 50%,#7d8171)"></div></div>
</section>

<!-- Referenzen -->
<section class="section" style="top:1606px">
  <div class="section-head"><div class="head-bar left"></div><h2 class="section-title">Referenzen</h2><div class="head-bar right"></div></div>
  <div class="content" style="top:29px">
    <div class="subtitle">Gerüstbau, Fliesen- Schlosser- Malerarbeiten</div>
    <p style="margin-top:17px">Wir führen Objekte in verschiedenen Größenordnung aus. Es werden auch Baustellen als Generalunternehmer ausgeführt. Hierbei arbeiten wir ausschließlich mit langjährigen, zuverlässigen Partnern zusammen (Gerüstbau, Fliesen- Schlosser- Malerarbeiten). Anbei unter anderen folgende Objekte, um sich einen Überblick über unser umfassendes Leistungsspektrum zu verschaffen.</p>
    <ul class="num-list" style="margin-top:20px">
      <li><span class="badge">1</span>Gewerbliche Objekte</li>
      <li><span class="badge">2</span>Private Objekte</li>
    </ul>
    <div class="block-head" style="margin-top:30px">Gewerbliche Objekte</div>
  </div>
  <div class="photo" style="left:715px;top:65px;width:220px;height:147px"><div role="img" aria-label="Foto: sanierter mehrstöckiger Bürobau" style="background:linear-gradient(180deg,#7f9fc9,#b9c2c8 40%,#8c9579 85%,#5f6f43)"></div></div>
</section>

<div class="photo" style="left:288px;top:1864px;width:307px;height:200px"><div role="img" aria-label="Foto: Brücke vor der Sanierung" style="background:linear-gradient(180deg,#b9b9b0,#8b8a82 45%,#6f7a55)"></div></div>
<div class="photo" style="left:624px;top:1864px;width:311px;height:200px"><div role="img" aria-label="Foto: Brücke nach der Sanierung" style="background:linear-gradient(180deg,#c4c6c0,#a5a79e 45%,#7f944f)"></div></div>
<div class="cmp-label" style="left:286px;top:2071px">Vorher</div>
<div class="cmp-label" style="left:625px;top:2071px">Nachher</div>
<div class="slide-arrow l" style="top:2115px"></div>
<div class="thumbs" style="top:2102px" role="img" aria-label="Vorschaubilder der gewerblichen Objekte">
  <div style="background:#7f8378"></div><div style="background:#939689"></div><div style="background:#8a8c80"></div><div style="background:#7a7f6c"></div><div style="background:#90928a"></div><div style="background:#6f7a55"></div><div style="background:#888b80"></div><div style="background:#7c8470"></div>
  <span class="sel"></span>
</div>
<div class="slide-arrow r" style="top:2115px"></div>

<div class="block-head abs" style="left:286px;top:2178px">Private Objekte</div>
<div class="photo" style="left:288px;top:2204px;width:307px;height:202px"><div role="img" aria-label="Foto: Wohnhaus mit Balkonen vor der Sanierung" style="background:linear-gradient(180deg,#a4a49e,#8a8a84 60%,#6c7860)"></div></div>
<div class="photo" style="left:624px;top:2204px;width:311px;height:202px"><div role="img" aria-label="Foto: Wohnhaus mit Balkonen nach der Sanierung" style="background:linear-gradient(180deg,#8fa9cf,#c3c6c4 45%,#8e9c73)"></div></div>
<div class="cmp-label" style="left:286px;top:2413px">Vorher</div>
<div class="cmp-label" style="left:625px;top:2413px">Nachher</div>
<div class="slide-arrow l" style="top:2453px"></div>
<div class="thumbs" style="top:2441px" role="img" aria-label="Vorschaubilder der privaten Objekte">
  <div style="background:#9a9a92"></div><div style="background:#a7aca9"></div><div style="background:#8e8e88"></div><div style="background:#9ea6b4"></div><div style="background:#8b8c84"></div><div style="background:#9aa3ac"></div><div style="background:#8f918a"></div><div style="background:#a3a9b2"></div>
  <span class="sel"></span>
</div>
<div class="slide-arrow r" style="top:2453px"></div>

<!-- Kontakt -->
<section class="section" style="top:2542px">
  <div class="section-head"><div class="head-bar left"></div><h2 class="section-title">Kontakt</h2><div class="head-bar right"></div></div>
  <div class="content" style="top:29px">
    <div class="subtitle">K+W Bautenschutz Kontaktinformationen</div>
    <div style="margin-top:20px;font-size:8.5px">K+W Bautenschutz GmbH</div>
    <div style="display:flex;gap:80px;margin-top:12px;font-size:8.5px;line-height:12px">
      <div>Werftstraße 12<br>68799 Reilingen</div>
      <div>Tel.:&nbsp;&nbsp;&nbsp;(0 62 05) 41 18 20<br>Fax:&nbsp;&nbsp;&nbsp;(0 62 05) 41 18 21<br>E-Mail: info@kw-bautenschutz.de</div>
    </div>
    <div class="block-head" style="margin-top:30px">Kontaktieren Sie uns direkt!</div>
  </div>
</section>

<div class="field" style="left:286px;top:2736px;width:180px">Name/Vorname*</div>
<div class="field" style="left:477px;top:2736px;width:178px">Firma</div>
<div class="field" style="left:286px;top:2772px;width:180px">Straße</div>
<div class="field" style="left:477px;top:2772px;width:178px">PLZ/Ort</div>
<div class="field" style="left:286px;top:2809px;width:180px">Telefon</div>
<div class="field" style="left:477px;top:2809px;width:178px">Fax</div>
<div class="field" style="left:286px;top:2845px;width:180px">E-Mail*</div>
<div class="field" style="left:286px;top:2881px;width:369px;height:140px">Nachricht*</div>

<div class="captcha">
  <span class="box"></span><span class="label">Ich bin kein Roboter.</span>
  <span class="mark"></span><span class="fine">Sicherheitsprüfung<br>Datenschutz · Nutzung</span>
</div>
<div class="submit">Absenden</div>
<div class="map" role="img" aria-label="Karte: Standort Werftstraße 12 in Reilingen"></div>

<!-- Karriere -->
<section class="section" style="top:3406px">
  <div class="section-head"><div class="head-bar left"></div><h2 class="section-title">Karriere</h2><div class="head-bar right"></div></div>
  <div class="content" style="top:29px">
    <div class="subtitle">Jobs bei K+W Bautenschutz</div>
    <div class="intro" style="margin-top:18px;font-size:9.5px;line-height:12px">Wir bieten Jobs im Bereich Gerüstbau, Fliesen- Schlosser- Malerarbeiten</div>
    <div style="line-height:12px">Hier finden Sie unsere aktuellen Stellenangebote:</div>
    <div class="block-head" style="margin-top:40px">Vorarbeiter und Facharbeiter</div>
    <p style="margin-top:13px">Für die Betonsanierung wird bald möglichst ein neuer Mitarbeiter gesucht.<br>Entsprechende Kenntnisse B ein Führerschein sind erforderlich.</p>
    <p>Schicken Sie Ihre Bewerbung per E-Mail, oder wenden Sie sich mit<br>dem Kontaktformular an uns.</p>
    <p>Gerne können Sie auch Ihre Bewerbungsunterlagen auf dem Postweg<br>zukommen lassen:</p>
    <p>K+W Bautenschutz GmbH, Werftstraße 12, 68799 Reilingen T. 06205-411820</p>
    <div class="pager" style="margin-top:18px">
      <div class="arrow-l"></div><div class="num">1</div><div class="num">2</div><div class="num">3</div><div class="num">4</div><div class="arrow-r"></div>
    </div>
  </div>
  <div class="photo" style="left:679px;top:143px;width:256px;height:164px"><div role="img" aria-label="Illustration: Aufstieg auf einer Karriere-Treppe vor hellblauem Büro" style="background:linear-gradient(160deg,#dbeefb,#8ec8ef 55%,#4aa3df)"></div></div>
</section>

<footer class="site-footer">
  <div class="foot-links"><span>Kontakt</span><span>Karriere</span><span>Impressum</span><span>Datenschutz</span></div>
  <div class="copyright">© K+W Bautenschutz GmbH 2019. All Rights Reserved.</div>
</footer>

</body>
</html>
```